Quarrow financial services, is a financial company that provides consultancy, brokerage services, and funding.

we will be providing the clients with insights, knowledge and data with regards to the financial markets.

with the brokerage services we will try to find the suitable counterparts that provide them with the best investments that suits their needs and expected return.

Target Market(s)

financial institutions, Corporates, high-net worth individuals

Industry/Entity Type

Financial Service

Contact Information for Business Card

Font styles to use
Other font styles liked:
• applemyungjo

Colors
00a990
848484

Requirements
Must have
• the logo at the back
Nice to have
• Finesse
Should not have
• boldness

```html
<!DOCTYPE html>
<html lang="en">
<head>
<meta charset="utf-8">
<title>Quarrow Financial Services – Business Card</title>
<link rel="stylesheet" href="https://fonts.googleapis.com/css2?family=Montserrat:wght@300;400;500&display=swap">
<style>
  :root {
    --backdrop: #2e2f31;
    --card-white: #fbfbfa;
    --card-shade: #efefed;
    --leaf-green: #7fa23a;
    --leaf-green-dark: #6b8c2e;
    --leaf-green-light: #a9c07a;
    --ink: #4a4a4a;
    --mark-grey: #d9d9d7;
    --mark-grey-faint: #eeeeec;
  }
  * { box-sizing: border-box; margin: 0; padding: 0; }
  html, body {
    width: 1200px; height: 843px; overflow: hidden;
    background: var(--backdrop);
    font-family: "Montserrat", Arial, sans-serif;
  }
  .canvas {
    position: relative; width: 1200px; height: 843px;
    display: flex; align-items: center; justify-content: center; gap: 56px;
  }
  .card {
    position: relative; width: 540px; height: 309px;
    border-radius: 3px; overflow: hidden;
  }

  /* Back side */
  .card--back {
    background: linear-gradient(135deg, var(--leaf-green-light) -40%, var(--leaf-green) 45%, var(--leaf-green-dark) 120%);
  }
  .back-mark {
    position: absolute; left: 50%; top: 50%; transform: translate(-50%, -50%);
    display: flex; align-items: center; gap: 14px;
  }
  .back-mark__square { width: 38px; height: 38px; background: var(--mark-grey); }
  .back-mark__name {
    color: #f6f6f4; font-weight: 400; font-size: 26px; letter-spacing: 4px;
    text-transform: uppercase;
  }

  /* Front side */
  .card--front {
    background: linear-gradient(180deg, var(--card-white) 0%, var(--card-white) 55%, var(--card-shade) 100%);
  }
  .front-watermark {
    position: absolute; left: 64px; top: 26px; width: 150px; height: 180px;
    background: var(--mark-grey-faint); opacity: .7;
  }
  .holder { position: absolute; left: 82px; top: 98px; }
  .holder__name {
    color: var(--leaf-green); font-weight: 500; font-size: 15px; letter-spacing: .8px;
    text-transform: uppercase;
  }
  .holder__title { color: var(--ink); font-weight: 400; font-size: 12.5px; margin-top: 3px; }

  .divider {
    position: absolute; left: 64px; top: 150px; width: 412px; height: 1px;
    background: var(--leaf-green);
  }
  .divider__sprig {
    position: absolute; right: -26px; top: -4px; width: 26px; height: 9px;
    border-radius: 50%; background: var(--leaf-green);
  }
  .contact { position: absolute; left: 66px; top: 160px; list-style: none; }
  .contact__item {
    display: flex; align-items: center; gap: 10px;
    color: var(--ink); font-size: 12.5px; font-weight: 400; height: 19px;
  }
  .contact__icon { width: 12px; height: 12px; flex: none; }

  .brand {
    position: absolute; right: 40px; top: 26px;
    display: flex; flex-direction: column; align-items: center; gap: 8px;
  }
  .brand__square { width: 40px; height: 40px; background: var(--mark-grey); }
  .brand__name {
    color: var(--ink); font-weight: 400; font-size: 20px; letter-spacing: 3px;
    text-transform: uppercase; text-align: center; line-height: 1.2;
  }
  .brand__tagline {
    color: var(--ink); font-weight: 400; font-size: 10.5px; letter-spacing: 2px;
    text-transform: uppercase; text-align: center; margin-top: -4px;
  }

  .address {
    position: absolute; right: 40px; top: 236px; font-style: normal;
    color: var(--ink); font-size: 12.5px; font-weight: 400; line-height: 1.5;
  }
</style>
</head>
<body>
<main class="canvas">

  <section class="card card--back" aria-label="Card back">
    <div class="back-mark">
      <span class="back-mark__square"></span>
      <span class="back-mark__name">Quarrow</span>
    </div>
  </section>

  <section class="card card--front" aria-label="Card front">
    <div class="front-watermark"></div>

    <div class="brand">
      <span class="brand__square"></span>
      <p class="brand__name">Quarrow</p>
      <p class="brand__tagline">Financial Services</p>
    </div>

    <div class="holder">
      <p class="holder__name">Mara Lindqvist</p>
      <p class="holder__title">President</p>
    </div>

    <div class="divider">
      <span class="divider__sprig" role="img" aria-label="Small leaf sprig ornament"></span>
    </div>

    <ul class="contact">
      <li class="contact__item">
        <svg class="contact__icon" viewBox="0 0 12 12" aria-hidden="true">
          <circle cx="6" cy="6" r="6" fill="var(--leaf-green)"/>
          <path d="M3.4 4.2c0-.5.4-.8.8-.8h.6l.6 1.4-.6.5c.3.7.8 1.2 1.5 1.5l.5-.6 1.4.6v.6c0 .4-.3.8-.8.8C5.3 8.2 3.4 6.3 3.4 4.2z" fill="#fff"/>
        </svg>
        <span>555 0142 7789</span>
      </li>
      <li class="contact__item">
        <svg class="contact__icon" viewBox="0 0 12 12" aria-hidden="true">
          <circle cx="6" cy="6" r="6" fill="var(--leaf-green)"/>
          <rect x="3" y="4" width="6" height="4.2" fill="#fff"/>
          <path d="M3 4l3 2.3L9 4" fill="none" stroke="var(--leaf-green)" stroke-width=".7"/>
        </svg>
        <span>mara@quarrowfinance.com</span>
      </li>
      <li class="contact__item">
        <svg class="contact__icon" viewBox="0 0 12 12" aria-hidden="true">
          <circle cx="6" cy="6" r="6" fill="var(--leaf-green)"/>
          <circle cx="6" cy="6" r="3" fill="none" stroke="#fff" stroke-width=".8"/>
          <path d="M3 6h6M6 3c-1.2 1.6-1.2 4.4 0 6M6 3c1.2 1.6 1.2 4.4 0 6" fill="none" stroke="#fff" stroke-width=".6"/>
        </svg>
        <span>www.quarrowfinance.com</span>
      </li>
    </ul>

    <address class="address">
      1420 Alder Crest Road<br>
      Brookmere, NY 11098
    </address>
  </section>

</main>
</body>
</html>
```